Flyer-Design für Tauchunternehmen
Aufmerksamer und sehr kompetenter Designer. Änderungswünsche werden umgehend umgesetzt. Ich bin sehr zufrieden und glücklich mit dem neuen Flyer.
Zielgruppe
Wir sind ein Tauchunternehmen in Ägypten und organisieren Tauchsafaris von 1 Tag bis 1 Woche im südlichen Roten Meer. In diesem Flyer geht es vor allem um Sataya, welches voll und ganz im Zeichen von Delfinen steht. Unsere Zielgruppe sind Vollblut Taucher, sowie auch Schnorchelturisten, welche 1 Tag dort verbringen wollen. Was ebenfalls in Sataya populär ist, ist Yoga auf dem Boot, Meditationen etc. „mit den Delfinen'.
Es soll daraus hervor gehen, dass Sataya für Schnorchler, wie auch Taucher geeignet ist (Tauchen mit den Delfinen ist nicht erlaubt)
Aufgabenstellung
Super wäre es, die Flyer in Deutsch und Englisch zu haben. Oder in so einem Format zu bekommen, dass ich die Texte selber austauschen kann. Kein Spezialprogramm oder Kenntnisse meinerseits vorhanden. PDF kann ggt. konvertiert werden in Word. Die Texte sind wie folgt, können auch noch angepasst werden. Mehr Bilder sind vorhanden vorallem von den Delfinen.
Sataya
Let the dolphins touch your soul
Full charter/Mini Safari/Overnight/Daily boat
Sataya, Fury Shoals
Two hours by boat from Hamata port, there is the horseshoe reef of Sataya, home of a large school of spinner dolphins.
With us, you have the opportunity to swim and snorkel with the dolphins ethically. The reef offers various levels of difficulty for divers, from easy dives inside the reef to more challenging dives on the steep walls on the outside the reef.
Full charter
If you are a group that would like to be together for a week, then a full charter might be the right choice for you. Discover the beautiful destinations of Fury Shoals and St. John’s while diving and snorkeling for a week. We will give our best to fulfil your wishes and give you an unforgettable experience.
Mini safari
Would you like to know how it feels like to be on a liveaboard without being on the boat for the whole week? Then take a part in mini safari where you can spend 2 nights at sea and enjoy the time snorkeling and diving in different places in Fury Shoals.
Overnight
Take a short break. Enjoy the sun, the stars, and the sea. Experience the beauty of Sataya and spend a night on the boat. Explore the colourful reefs during your dives, or swim and snorkel with the dolphins and let them touch your soul.
Daily boat
Enjoy a day in Sataya. Swim and snorkel with the dolphins, enjoy a delicious lunch and go snorkeling again.
The tours depart from and return to the port of Hamata.
Our boats, Nawrin and Tibor 1, fully a..

```html
<!DOCTYPE html>
<html lang="de">
<head>
<meta charset="utf-8">
<title>Lass die Delfine deine Seele berühren</title>
<link rel="stylesheet" href="https://fonts.googleapis.com/css2?family=Montserrat:wght@300;400;700&display=swap">
<style>
:root{
  --slate:#4a5878;
  --ink:#3f4b66;
  --white:#ffffff;
}
*{margin:0;padding:0;box-sizing:border-box}
html,body{width:1200px;height:848px;overflow:hidden;background:var(--white)}
body{font-family:"Montserrat",sans-serif;color:var(--ink);position:relative}
.photo{position:absolute;overflow:hidden}

/* photo areas: soft gradients in the main tones of each scene */
.yacht-calm{background:
  radial-gradient(ellipse 70% 18% at 55% 66%,rgba(255,255,255,.55),rgba(255,255,255,0) 70%),
  linear-gradient(180deg,#cfe3f3 0%,#dcebf6 30%,#b9d5ec 55%,#5d97c9 64%,#2f75b4 78%,#1d5f9e 100%)}
.yacht-open{background:
  radial-gradient(ellipse 65% 22% at 62% 48%,rgba(245,245,245,.7),rgba(245,245,245,0) 70%),
  radial-gradient(ellipse 55% 10% at 60% 60%,rgba(35,50,100,.55),rgba(35,50,100,0) 70%),
  linear-gradient(180deg,#8f9fb8 0%,#aeb6c6 30%,#9aa9bf 55%,#3f77ac 62%,#2a68a3 80%,#1f5a92 100%)}
.reef-horizon{background:
  radial-gradient(ellipse 35% 14% at 30% 62%,rgba(60,110,110,.75),rgba(60,110,110,0) 70%),
  radial-gradient(ellipse 30% 10% at 75% 58%,rgba(60,110,110,.6),rgba(60,110,110,0) 70%),
  radial-gradient(ellipse 25% 18% at 55% 100%,rgba(180,110,60,.8),rgba(180,110,60,0) 70%),
  linear-gradient(180deg,#7a8fc4 0%,#8ea3cc 22%,#2f8fc8 32%,#1f78b8 60%,#15609e 100%)}
.reef-aerial{background:
  radial-gradient(ellipse 60% 30% at 65% 25%,rgba(120,170,150,.55),rgba(120,170,150,0) 70%),
  radial-gradient(ellipse 20% 9% at 42% 55%,rgba(240,240,240,.75),rgba(240,240,240,0) 70%),
  radial-gradient(ellipse 40% 25% at 30% 80%,rgba(20,70,100,.6),rgba(20,70,100,0) 70%),
  linear-gradient(160deg,#2e7c8c 0%,#1f6a86 45%,#174f70 100%)}
.pod-deep{background:
  radial-gradient(ellipse 40% 30% at 40% 55%,rgba(110,140,170,.55),rgba(110,140,170,0) 70%),
  radial-gradient(ellipse 30% 35% at 75% 40%,rgba(120,150,180,.45),rgba(120,150,180,0) 70%),
  radial-gradient(ellipse 80% 25% at 50% 0%,rgba(160,220,250,.7),rgba(160,220,250,0) 70%),
  linear-gradient(180deg,#3aa2e0 0%,#1f7cc0 50%,#145a98 100%)}
.pod-bright{background:
  radial-gradient(ellipse 35% 30% at 40% 65%,rgba(200,110,100,.65),rgba(200,110,100,0) 70%),
  radial-gradient(ellipse 25% 15% at 50% 25%,rgba(190,140,140,.5),rgba(190,140,140,0) 70%),
  radial-gradient(ellipse 20% 12% at 85% 35%,rgba(100,120,140,.4),rgba(100,120,140,0) 70%),
  linear-gradient(180deg,#5ab8ea 0%,#45a6de 55%,#3b9ad6 100%)}
.snorkel-reef{background:
  radial-gradient(ellipse 18% 40% at 48% 45%,rgba(200,150,120,.45),rgba(200,150,120,0) 70%),
  linear-gradient(180deg,#5aa8a8 0%,#3e8a88 35%,#4f7466 65%,#6f7a60 100%)}
.deck-bar{background:
  radial-gradient(ellipse 25% 30% at 50% 35%,rgba(40,80,150,.55),rgba(40,80,150,0) 70%),
  linear-gradient(180deg,#e8eef2 0%,#f4f6f7 35%,#9fb3c2 45%,#e6e8e8 55%,#b88a60 75%,#7a5433 100%)}
.deck-sun{background:
  radial-gradient(ellipse 60% 20% at 50% 40%,rgba(60,110,160,.6),rgba(60,110,160,0) 70%),
  linear-gradient(180deg,#8a7a68 0%,#c9b8a0 22%,#e0d8cc 35%,#c49a6c 60%,#8a6440 100%)}
.salon-dark{background:
  radial-gradient(ellipse 50% 30% at 50% 25%,rgba(230,220,200,.45),rgba(230,220,200,0) 70%),
  linear-gradient(180deg,#4a3e36 0%,#8c7a66 45%,#d8d0c0 70%,#3e342e 100%)}
.cabin-navy{background:
  radial-gradient(ellipse 45% 30% at 65% 60%,rgba(170,110,60,.6),rgba(170,110,60,0) 70%),
  linear-gradient(180deg,#6a7488 0%,#2c3858 50%,#1f2a48 100%)}
.salon-azure{background:
  radial-gradient(ellipse 40% 20% at 50% 42%,rgba(60,170,220,.8),rgba(60,170,220,0) 70%),
  linear-gradient(180deg,#e6d6a8 0%,#a8b8c0 30%,#3f7fb0 55%,#7a5a3c 80%,#4a3624 100%)}
.cabin-rose{background:
  radial-gradient(ellipse 40% 25% at 30% 65%,rgba(40,80,170,.7),rgba(40,80,170,0) 70%),
  linear-gradient(180deg,#c8d0ec 0%,#7a88d0 40%,#a86aa0 70%,#e06088 100%)}

.boat-band{position:absolute;top:247px;width:300px;height:45px;background:var(--slate);color:var(--white);
  font-weight:700;font-size:25px;text-align:center;line-height:45px;letter-spacing:-.3px}
.boat-info{position:absolute;width:300px;text-align:center;font-weight:400}
.built{font-size:14px}
.spec{font-size:14.4px;line-height:17px;padding:0 14px}
.spec b{font-weight:700}
.guests{font-size:15px;font-weight:700;display:flex;justify-content:center;align-items:center;gap:8px}
.boat-desc{position:absolute;width:300px;padding:0 20px;text-align:center;font-size:9.8px;font-weight:300;line-height:12px;color:var(--ink)}

.headline{position:absolute;left:300px;width:600px;top:14px;text-align:center;font-size:28px;font-weight:400;color:var(--slate)}
.timeline{position:absolute;left:599px;top:72px;width:2px;height:646px;background:var(--slate)}
.dot{position:absolute;left:595px;width:10px;height:10px;border-radius:50%;background:var(--slate)}
.stop-title{position:absolute;font-size:16.5px;font-weight:700;color:var(--slate)}
.stop-text{position:absolute;font-size:9.8px;font-weight:300;line-height:12px;width:256px}
.left-side{right:623px;text-align:right}
.right-side{left:623px;text-align:left}
.footer{position:absolute;left:300px;width:600px;text-align:center;font-size:11.5px;font-weight:300;line-height:17.5px}
</style>
</head>
<body>

<!-- Tibor 1 -->
<div class="photo yacht-calm" style="left:0;top:0;width:300px;height:247px" role="img" aria-label="Weisse Motoryacht Tibor 1 vor Anker auf ruhigem blauem Meer"></div>
<div class="boat-band" style="left:0">MY Tibor 1</div>
<div class="boat-info" style="left:0;top:296px">
  <p class="built">wurde 2021 gebaut</p>
  <p class="spec" style="margin-top:10px">Mit einer Länge von <b>32</b> Meter und <b>8</b> Meter Breite bietet das aus Stahl konstruierte Boot bequem Platz für</p>
  <p class="guests" style="margin-top:6px"><svg width="14" height="24" viewBox="0 0 14 24" fill="none" stroke="#4a5878" stroke-width="1.6"><circle cx="7" cy="5" r="3.6"/><path d="M3 11c0-2 8-2 8 0v5c0 1-1 1.5-2 1.5v5h-4v-5c-1 0-2-.5-2-1.5z"/></svg>24 Gäste</p>
  <p class="spec" style="margin-top:4px">8 Kabinen mit zwei Einzelbetten befinden sich im Unterdeck und 4 Kabinen auf dem Oberdeck</p>
</div>
<p class="boat-desc" style="left:0;top:506px">Im Restaurant auf dem Hauptdeck werden 3 Buffets pro Tag serviert und auf dem grosszügigen Tauchdeck macht man sich für die Abenteuer bereit. Auf dem Oberdeck gibt es viele schattige Sitzmöglichkeiten und eine Bar für ein gemütliches Zusammensein und zum Entspannen. Auf dem Topdeck warten gemütli&shy;che Liegen. Ideal um die Sonne zu geniessen oder die Sterne zu beobachten.</p>
<div class="photo deck-bar" style="left:0;top:607px;width:300px;height:119px" role="img" aria-label="Überdachtes Oberdeck mit Bar, Sitzbänken und Holzboden"></div>
<div class="photo salon-dark" style="left:0;top:730px;width:148px;height:118px" role="img" aria-label="Salon mit Sitzgruppen und Tischen"></div>
<div class="photo cabin-navy" style="left:152px;top:730px;width:148px;height:118px" role="img" aria-label="Kabine mit zwei Einzelbetten"></div>

<!-- Tours -->
<h1 class="headline">Lass die Delfine deine Seele berühren</h1>
<div class="timeline"></div>
<div class="dot" style="top:67px"></div>
<div class="dot" style="top:243px"></div>
<div class="dot" style="top:410px"></div>
<div class="dot" style="top:562px"></div>
<div class="dot" style="top:713px"></div>

<h2 class="stop-title left-side" style="top:61px">Sataya, Fury Shoals</h2>
<p class="stop-text left-side" style="top:98px">Zwei Stunden mit dem Boot vom Hafen Hamata entfernt liegt das Riff von Sataya, Heimat einer grossen Schule Spinnerdelfinen. Mit uns hast du die Möglichkeit, mit den Delfinen in ihrer natürlichen Umgebung zu schwimmen und zu schnorcheln. Das Riff bietet unterschiedliche Plätze für Taucher, von einfachen Tauchgängen innerhalb des Riffs, bis hin zu anspruchsvolleren Tauchgängen an den Steilwänden an der Aussenseite des Riffs.</p>
<div class="photo reef-horizon" style="left:621px;top:65px;width:251px;height:144px" role="img" aria-label="Blick vom Bug eines Bootes auf Riffe im blauen Meer"></div>

<div class="photo reef-aerial" style="left:327px;top:234px;width:251px;height:141px" role="img" aria-label="Luftaufnahme einer Yacht in Fahrt über dem Riff"></div>
<h2 class="stop-title right-side" style="top:237px">Vollcharter</h2>
<p class="stop-text right-side" style="top:275px;width:248px">Wenn ihr eine Gruppe seid, die eine Woche lang zusammen sein möchte, dann ist ein Vollcharter vielleicht die richtige Wahl für euch. Entdecke die wunderschönen Ziele von Fury Shoals und St. Johns und tauche und schnorchle eine Woche lang. Wir werden unser Bestes geben, um eure Wünsche zu erfüllen und euch ein unvergessliches Erlebnis zu bescheren.</p>

<h2 class="stop-title left-side" style="top:403px">Mini safari</h2>
<p class="stop-text left-side" style="top:440px">Möchtest du wissen, wie es sich anfühlt, auf einer Tauchsafari zu sein, ohne die ganze Woche auf dem Boot zu sein? Dann nimm an der Mini-Safari teil, bei der du 2 Nächte auf dem Meer verbringst und die Zeit beim Schnorcheln und Tauchen an verschiedenen Orten in Fury Shoals geniesst.</p>
<div class="photo pod-deep" style="left:621px;top:400px;width:249px;height:126px" role="img" aria-label="Gruppe von Spinnerdelfinen unter Wasser"></div>

<div class="photo pod-bright" style="left:327px;top:551px;width:251px;height:128px" role="img" aria-label="Delfine schwimmen im hellblauen Wasser"></div>
<h2 class="stop-title right-side" style="top:556px">Overnight</h2>
<p class="stop-text right-side" style="top:594px">Mach eine kurze Pause. Geniesse die Sonne, die Sterne und das Meer. Erlebe die Schönheit von Sataya und verbringe eine Nacht auf dem Boot. Entdecke die farbenfrohen Riffe während deiner Tauchgänge oder schwimme und schnorchle mit den Delfinen und lass sie deine Seele berühren.</p>

<h2 class="stop-title left-side" style="top:707px">Tagesboot</h2>
<p class="stop-text left-side" style="top:744px">Fahre für einen Tag nach Sataya. Schwimme und Schnorchle mit den Delfinen, geniesse ein leckeres Mittagessen und geh nochmals Schnorchel.</p>
<div class="photo snorkel-reef" style="left:621px;top:704px;width:251px;height:88px" role="img" aria-label="Schnorchler über einem Korallenriff"></div>

<p class="footer" style="top:802px">Die Touren beginnen und enden im Hafen von Hamata<br>blauwellen-tauchsafari.com</p>

<!-- Nawrin -->
<div class="photo yacht-open" style="left:900px;top:0;width:300px;height:247px" role="img" aria-label="Weiss-blaue Motoryacht Nawrin auf dem offenen Meer"></div>
<div class="boat-band" style="left:900px">MY Nawrin</div>
<div class="boat-info" style="left:900px;top:296px">
  <p class="built">wurde 2019 gebaut</p>
  <p class="spec" style="margin-top:10px">Mit einer Länge von <b>30</b> Metern und einer Breite von <b>8</b> Metern bietet das aus Stahl konstruierte Boot bequem Platz für</p>
  <p class="guests" style="margin-top:6px"><svg width="14" height="24" viewBox="0 0 14 24" fill="none" stroke="#4a5878" stroke-width="1.6"><circle cx="7" cy="5" r="3.6"/><path d="M3 11c0-2 8-2 8 0v5c0 1-1 1.5-2 1.5v5h-4v-5c-1 0-2-.5-2-1.5z"/></svg>18 Gäste</p>
  <p class="spec" style="margin-top:4px">5 Kabinen mit zwei Einzelbetten und<br>2 Doppelbettkabinen befinden sich im Unterdeck und 2 Einzelbettkabinen auf dem Oberdeck</p>
</div>
<p class="boat-desc" style="left:900px;top:506px">Im Restaurant auf dem Hauptdeck werden 3 Buffets pro Tag serviert und auf dem grosszügigen Tauchdeck macht man sich für die Abenteuer bereit. Auf dem Oberdeck gibt es viele schattige Sitzmöglichkeiten und eine Bar für ein gemütliches Zusammensein und zum Entspannen. Auf dem Topdeck warten gemütli&shy;che Liegen. Ideal um die Sonne zu geniessen oder die Sterne zu beobachten.</p>
<div class="photo deck-sun" style="left:900px;top:607px;width:300px;height:119px" role="img" aria-label="Sonnendeck mit Leiter, Holzboden und Sitzecke"></div>
<div class="photo salon-azure" style="left:900px;top:730px;width:148px;height:118px" role="img" aria-label="Salon mit blauen Sofas und Buffet"></div>
<div class="photo cabin-rose" style="left:1052px;top:730px;width:148px;height:118px" role="img" aria-label="Kabine mit Betten und bunter Bettwäsche"></div>

</body>
</html>
```